Stationary set for consulting company
Tarvo Bridge
Creative Brief
Modern
Karim Yusuf Al Banna
Co-Founder
Reef Spire, Abu Dhabi United Arab Emirates
karim@tarvobridge.ae
www.tarvobridge.com
I need a full stationary set for the company logo I will be attaching. (PPTs, business cards, envelope, letterhead, etc)

```html
<!DOCTYPE html>
<html lang="en">
<head>
<meta charset="utf-8">
<title>Tarvo Bridge Consulting – Stationery Set</title>
<link href="https://fonts.googleapis.com/css2?family=Montserrat:wght@400;500;600;700&display=swap" rel="stylesheet">
<style>
  :root {
    --navy: #27468b;
    --paper: #ffffff;
    --stage: #f3f4f6;
    --ink: #2b2b2b;
    --muted: #8a8f99;
    --shadow: 0 6px 18px rgba(20, 30, 60, 0.18);
  }
  * { box-sizing: border-box; margin: 0; padding: 0; }
  html, body { width: 1200px; height: 939px; overflow: hidden; }
  body {
    position: relative;
    background: var(--stage);
    font-family: "Montserrat", Arial, sans-serif;
    color: var(--ink);
  }
  address { font-style: normal; }

  .brand-name {
    font-weight: 700;
    letter-spacing: 0.04em;
    text-transform: uppercase;
    line-height: 1;
    white-space: nowrap;
  }

  .side-label {
    position: absolute;
    top: 190px;
    font-size: 13px;
    font-weight: 700;
    color: #222;
  }
  .side-label--front { left: 140px; }
  .side-label--back { left: 436px; }

  /* Letterhead */
  .letterhead {
    position: absolute;
    left: 519px; top: 25px;
    width: 651px; height: 854px;
    background: var(--paper);
    box-shadow: var(--shadow);
    z-index: 1;
  }
  .letterhead__band {
    height: 92px;
    background: var(--navy);
    padding: 36px 0 0 16px;
  }
  .letterhead__band .brand-name { color: #fff; font-size: 20px; }
  .letterhead__recipient {
    position: absolute; left: 66px; top: 205px;
    font-size: 7px; line-height: 10px; color: var(--muted);
  }
  .letterhead__recipient strong {
    display: block; font-size: 11px; line-height: 15px;
    color: var(--ink); font-weight: 700; letter-spacing: 0.03em;
  }
  .letterhead__date {
    position: absolute; right: 40px; top: 223px;
    font-size: 7px; color: var(--muted);
  }
  .letterhead__greeting {
    position: absolute; left: 66px; top: 338px;
    font-size: 9px; font-weight: 700; color: var(--ink);
  }
  .letterhead__body {
    position: absolute; left: 66px; top: 408px; width: 560px;
    font-size: 7px; line-height: 11px; color: var(--muted);
  }
  .letterhead__body p { margin-bottom: 26px; }
  .letterhead__contact {
    position: absolute; left: 8px; top: 754px;
    font-size: 8px; line-height: 11px; color: var(--navy);
  }
  .letterhead__mark {
    position: absolute; right: 22px; bottom: 26px;
    color: var(--navy); font-size: 11px;
  }
  .letterhead__footer-band {
    position: absolute; left: 0; right: 0; bottom: 0; height: 9px;
    background: var(--navy);
  }

  /* Envelope */
  .envelope {
    position: absolute;
    left: 20px; top: 336px;
    width: 734px; height: 386px;
    background: var(--paper);
    box-shadow: var(--shadow);
    z-index: 2;
  }
  .envelope__band {
    height: 100px;
    background: var(--navy);
    padding: 46px 0 0 8px;
  }
  .envelope__band .brand-name { color: #fff; font-size: 20px; }
  .envelope__address {
    position: absolute; left: 8px; top: 106px;
    font-size: 8px; line-height: 11px; color: var(--navy);
  }
  .envelope__mark {
    position: absolute; right: 24px; bottom: 30px;
    color: var(--navy); font-size: 11px;
  }
  .envelope__footer-band {
    position: absolute; left: 0; right: 0; bottom: 0; height: 9px;
    background: var(--navy);
  }

  /* Business cards */
  .card {
    position: absolute;
    box-shadow: var(--shadow);
    z-index: 2;
    overflow: hidden;
  }
  .card--front {
    left: 43px; top: 217px; width: 203px; height: 117px;
    background: var(--paper);
  }
  .card__band {
    height: 46px; background: var(--navy);
    position: relative;
  }
  .card__band .brand-name {
    position: absolute; left: 6px; bottom: 7px;
    color: #fff; font-size: 10px;
  }
  .card__holder {
    position: absolute; right: 8px; top: 8px;
    text-align: right; color: #fff;
  }
  .card__holder-name { font-size: 7px; font-weight: 600; white-space: nowrap; }
  .card__holder-role { font-size: 5px; margin-top: 1px; }
  .card__contact {
    position: absolute; left: 6px; top: 56px;
    font-size: 4.5px; line-height: 6.5px; color: var(--navy);
  }
  .card__mark {
    position: absolute; right: 8px; bottom: 10px;
    color: var(--navy); font-size: 6px;
  }
  .card__footer-band {
    position: absolute; left: 0; right: 0; bottom: 0; height: 5px;
    background: var(--navy);
  }
  .card--back {
    left: 329px; top: 212px; width: 253px; height: 119px;
    background: var(--navy);
    display: flex; align-items: center; justify-content: center;
  }
  .card--back .brand-name { color: #fff; font-size: 14px; }
</style>
</head>
<body>

  <span class="side-label side-label--front">Front</span>
  <span class="side-label side-label--back">Back</span>

  <section class="letterhead">
    <header class="letterhead__band">
      <span class="brand-name">Tarvo Bridge</span>
    </header>
    <div class="letterhead__recipient">
      <strong>LENA MARLOW</strong>
      48 Harbor Lane,<br>Dover, DE 19901
    </div>
    <div class="letterhead__date">July 20, 2021</div>
    <div class="letterhead__greeting">Dear Lena Marlow,</div>
    <div class="letterhead__body">
      <p>A letterhead template is a ready-to-use format document containing information about your company with space for a personalized message. These assist in aligning your brand with all correspondence you send to your valued clients.</p>
      <p>The name of the company is arranged in the form of a header, typically with a logo. This provides a first understanding of the company and what they offer, which is also in line with the company name and stationery.</p>
      <p>It also carries information for a specific employee. This happens if the letter sets one particular department or sender rather than the entire organization.</p>
      <p>It is clear that the whole sheet is printed with such a heading. Many create a letterhead template in a word processor or other software with the same information as pre-printed stationery but without the cost.</p>
    </div>
    <address class="letterhead__contact">
      Reef Spire, Abu Dhabi<br>
      United Arab Emirates<br>
      Cell: +971 50 000 4418<br>
      Email: karim@tarvobridge.ae<br>
      Web: www.tarvobridge.com
    </address>
    <span class="letterhead__mark brand-name">Tarvo Bridge</span>
    <div class="letterhead__footer-band"></div>
  </section>

  <section class="envelope">
    <header class="envelope__band">
      <span class="brand-name">Tarvo Bridge</span>
    </header>
    <address class="envelope__address">
      Reef Spire, Abu Dhabi<br>
      United Arab Emirates
    </address>
    <span class="envelope__mark brand-name">Tarvo Bridge</span>
    <div class="envelope__footer-band"></div>
  </section>

  <section class="card card--front">
    <header class="card__band">
      <span class="brand-name">Tarvo Bridge</span>
      <div class="card__holder">
        <div class="card__holder-name">Karim Yusuf Al Banna</div>
        <div class="card__holder-role">Co-Founder</div>
      </div>
    </header>
    <address class="card__contact">
      Reef Spire, Abu Dhabi<br>
      United Arab Emirates<br>
      Cell: +971 50 000 4418<br>
      Email: karim@tarvobridge.ae<br>
      Web: www.tarvobridge.com
    </address>
    <span class="card__mark brand-name">Tarvo Bridge</span>
    <div class="card__footer-band"></div>
  </section>

  <section class="card card--back">
    <span class="brand-name">Tarvo Bridge</span>
  </section>

</body>
</html>
```